Nice craft box with banderole or sticker

We want to get a packaging box design for the 3D puzzle. The packaging is craft paper print black or white, wrap with a banderole or wrap with a stikcer. This box should be designed in a minimalist style as much as possible, as shown in the attached file. Only the product photos are in color, and the colors of the box and packaging are relatively simple. The color of the banderole or adhesive should be suitable. Products of different colors can be placed on without conflict. If you have better ideas, it's also possible. our product name is 3D paper puzzle or 3D cardboard Model. it have animal puzzles, like birds, insect ,wild animal. it is for young chirdren. 5-12 years old. the design also can be similar as our file, but it should be better than it.

The box size is about : 12*19*1.2CM, Attach is some packing design ideal and our logo.
we like nice font for the text. and 1-3 nice icon.

We like more nice design. It can attract the eyes. We hope all items can be use same banderole, and just put different animal photo on it.

Also You can visit our website: www.velmaro.com. you can kow how about our product.

We attach 3 items photo. You can choose one to make the design. Our product is DIY, education. Animal with scene

Target Market(s)

Europe,Janpan,USA

Requirements
Must have
• Text is black for the craft box. nice color for the banderole or sticker.
Nice to have
• nice icon.
Should not have
• craft box should not be very colorful.

```html
<!DOCTYPE html>
<html lang="en">
<head>
<meta charset="utf-8">
<title>3D Paper Puzzle – Box Lid No 02</title>
<link rel="stylesheet" href="https://fonts.googleapis.com/css2?family=Bungee+Outline&family=Black+Ops+One&family=Russo+One&display=swap">
<style>
  :root {
    --page: #ffffff;
    --craft: #bb8b4f;
    --craft-edge: #a77a43;
    --ink: #1b1612;
    --label: #d9622a;
    --label-line: #f6d9c4;
    --photo-bg: #ffffff;
    --photo-sand: #c88d45;
    --photo-model: #9fb2d6;
  }
  * { box-sizing: border-box; margin: 0; padding: 0; }
  html, body { width: 1200px; height: 632px; overflow: hidden; background: var(--page); }
  .lid {
    position: absolute; left: 40px; top: 36px; width: 1120px; height: 560px;
    background: var(--craft); border: 1px solid var(--craft-edge);
    color: var(--ink); font-family: "Russo One", sans-serif;
  }
  .tag { position: absolute; display: flex; align-items: center; gap: 8px; font-style: italic; }
  .tag svg { width: 22px; height: 16px; }
  .tag--model { left: 70px; top: 38px; font-size: 13px; }
  .tag--journey { left: 70px; top: 420px; font-size: 17px; }
  .title { position: absolute; left: 70px; top: 80px; }
  .title__3d { font-family: "Bungee Outline", sans-serif; font-size: 150px; line-height: 1; letter-spacing: -4px; }
  .title__words { font-family: "Black Ops One", sans-serif; font-size: 62px; line-height: 0.95; letter-spacing: 8px; margin-top: 4px; }
  .bars { position: absolute; }
  .bars--top { left: 580px; top: 70px; }
  .bars--bottom { left: 560px; top: 418px; }
  .card { position: absolute; left: 560px; top: 130px; width: 500px; height: 270px; display: flex; }
  .card__label {
    width: 200px; background: var(--label); padding: 22px 16px 14px; color: var(--ink);
    display: flex; flex-direction: column; gap: 8px;
  }
  .card__no { font-size: 34px; line-height: 1; }
  .card__no sup { font-size: 13px; }
  .card__name { font-size: 15px; font-style: italic; border-top: 2px solid var(--label-line); padding-top: 8px; }
  .card__sub { font-size: 9px; opacity: .8; margin-top: -4px; }
  .card__spec { font-size: 12px; font-style: italic; border-top: 2px solid var(--label-line); padding-top: 6px; color: var(--label-line); }
  .card__photo { flex: 1; background: var(--photo-bg); padding: 14px; display: flex; flex-direction: column; gap: 10px; }
  .card__image {
    flex: 1; border-radius: 4px;
    background: linear-gradient(160deg, var(--photo-bg) 20%, var(--photo-model) 45%, var(--photo-sand) 75%, var(--photo-bg) 100%);
  }
  .card__steps { font-family: "Russo One", sans-serif; font-size: 9px; line-height: 1.5; color: var(--ink); }
  .brand { position: absolute; right: 40px; bottom: 30px; display: flex; align-items: center; gap: 8px; font-size: 14px; letter-spacing: 2px; }
  .brand__dot { width: 22px; height: 22px; border-radius: 50%; background: var(--ink); }
</style>
</head>
<body>
<main class="lid">
  <p class="tag tag--model">
    <svg viewBox="0 0 22 16" aria-hidden="true"><path d="M21 5H9l2-3H7L2 7v6l3 2h9v-2h-4m4 0V9h-4m4 0h5" fill="none" stroke="currentColor" stroke-width="1.6" stroke-linejoin="round"/></svg>
    PAPER MODEL
  </p>

  <h1 class="title">
    <div class="title__3d">3D</div>
    <div class="title__words">PAPER<br>PUZZLE</div>
  </h1>

  <p class="tag tag--journey">
    <svg viewBox="0 0 22 16" aria-hidden="true"><path d="M21 5H9l2-3H7L2 7v6l3 2h9v-2h-4m4 0V9h-4m4 0h5" fill="none" stroke="currentColor" stroke-width="1.6" stroke-linejoin="round"/></svg>
    CREATIVE JOURNEY
  </p>

  <svg class="bars bars--top" width="320" height="50" viewBox="0 0 320 50" aria-hidden="true" fill="var(--ink)">
    <rect x="0" y="14" width="8" height="36"/><rect x="16" y="4" width="10" height="46"/><rect x="34" y="0" width="12" height="50"/>
    <rect x="56" y="16" width="8" height="34"/><rect x="74" y="6" width="10" height="44"/><rect x="92" y="20" width="7" height="30"/>
    <rect x="108" y="10" width="9" height="40"/><rect x="126" y="24" width="6" height="26"/><rect x="142" y="14" width="8" height="36"/>
    <rect x="160" y="28" width="6" height="22"/><rect x="176" y="22" width="7" height="28"/><rect x="194" y="32" width="5" height="18"/>
    <rect x="210" y="30" width="6" height="20"/><rect x="226" y="38" width="5" height="12"/><rect x="240" y="36" width="5" height="14"/>
  </svg>

  <section class="card">
    <div class="card__label">
      <p class="card__no"><sup>N°</sup>02</p>
      <p class="card__name">TIRANOSAURIO REX</p>
      <p class="card__sub">Dinosaur Paper Model</p>
      <p class="card__spec">PARTS: 100 PCS</p>
      <p class="card__spec">SIZE: 90X30X60CM</p>
      <p class="card__spec">MATERIAL: PAPER</p>
    </div>
    <div class="card__photo">
      <div class="card__image" role="img" aria-label="Photo of the assembled blue paper dinosaur standing on a sandy scene base, with loose puzzle parts laid out"></div>
      <p class="card__steps">Step cards inside. Fold, slot and build your own model.</p>
    </div>
  </section>

  <svg class="bars bars--bottom" width="420" height="40" viewBox="0 0 420 40" aria-hidden="true" fill="var(--ink)">
    <polygon points="8,0 18,0 10,40 0,40"/><polygon points="30,0 42,0 34,40 22,40"/><polygon points="56,0 66,0 58,40 48,40"/>
    <polygon points="80,0 94,0 86,40 72,40"/><polygon points="108,0 116,0 110,30 102,30"/><polygon points="130,0 142,0 136,28 124,28"/>
    <polygon points="160,4 180,4 176,22 156,22"/><polygon points="200,6 214,6 210,20 196,20"/><polygon points="232,8 248,8 244,18 228,18"/>
    <polygon points="268,10 284,10 282,16 266,16"/><polygon points="302,12 314,12 312,16 300,16"/><polygon points="330,12 340,12 338,16 328,16"/>
  </svg>

  <div class="brand"><span class="brand__dot"></span>VELMARO</div>
</main>
</body>
</html>
```